A Clear Three Step Roadmap For Contractors

We are looking for a one-pager "roadmap" that is similar to the 2nd picture we attached, but much more professional & better... please make it landscape orientation. The logo for this system is attached below, as well.

Our Brand Colors to use:
#f2d582
#303030
#8b8c90

The copy we'd like to use on the flyer:
A Clear Three Step Roadmap that will finally allow you to attract quality customers and win more jobs.

The Keystone Ladder Method is a simple to follow system that was created specifically for Contractors and Blue Collar Business Owners.

When it comes to marketing and growing their business, the majority of Contractors are left confused, frustrated and extremely overwhelmed. Unlike most sales, marketing & training programs that offer a single "piece of the puzzle", we've mapped out each essential step of the puzzle and cut out all of the fluff.

All you have to do is complete each step in the right order and we'll be guiding you along the entire journey!

A ---> B

Blueprint: Get clear on where you're going, define your ideal audience, and finally, master your message.
Step 1: Clarify The Chaos
Step 2: Define Your Customer
Step 3: Master Your Message

Build: Attract quality leads, Build your funnel and Formulate a high-converting follow-up system
Step 4: Develop Lead Generator
Step 5: Construct Your Funnel
Step 6: Formulate the Follow-Up

Breakthrough: Get in front of your ideal customers and rapidly scale your business by driving traffic and becoming the authority in your market
Step 7: Turn-On the Traffic
Step 8: Become the Authority
Step 9: Unlock Your Growth

```html
<!DOCTYPE html>
<html lang="en">
<head>
<meta charset="utf-8">
<title>Keystone Ladder Method – Three Step Roadmap</title>
<link href="https://fonts.googleapis.com/css2?family=Lato:wght@400;700&family=Titillium+Web:wght@600;700&display=swap" rel="stylesheet">
<style>
  :root{
    --gold:#f2d582;
    --gold-soft:#e8cb7c;
    --ink:#262626;
    --charcoal:#303030;
    --steel:#8b8c90;
    --paper:#ffffff;
    --stage:#7a7a7a;
  }
  *{margin:0;padding:0;box-sizing:border-box}
  html,body{width:1200px;height:904px;overflow:hidden;background:var(--stage)}
  .flyer{position:absolute;left:0;top:114px;width:1200px;height:675px;background:var(--ink);overflow:hidden;font-family:"Lato",sans-serif}
  .flyer-bg{position:absolute;inset:0}
  .brand{position:absolute;left:0;right:0;top:30px;display:flex;justify-content:center;align-items:center;gap:14px;color:var(--paper);font-family:"Lato",sans-serif;font-weight:700}
  .brand-mark{width:58px;height:58px;background:var(--gold)}
  .brand-name{display:flex;flex-direction:column;line-height:1}
  .brand-name .line-sm{font-size:25px;letter-spacing:.2px}
  .brand-name .line-lg{font-size:44px;letter-spacing:2px;margin-top:3px}
  .tagline{position:absolute;left:0;right:0;top:134px;text-align:center;color:var(--paper);font-family:"Titillium Web",sans-serif;font-weight:700;font-size:19.5px;line-height:24px}
  .intro{position:absolute;left:30px;top:214px;width:248px;color:var(--ink);font-size:12.6px;line-height:16.1px;text-align:justify}
  .intro p{margin-bottom:16px}
  .intro .cta{position:absolute;top:264px;font-weight:700;color:#1c1c1c}
  .steps{position:absolute;left:925px;top:222px;width:260px}
  .step{position:relative;padding-left:73px;margin-bottom:0}
  .step-num{position:absolute;left:2px;top:4px;width:56px;height:56px;border:3px solid var(--ink);border-radius:50%;display:flex;align-items:center;justify-content:center;font-family:"Titillium Web",sans-serif;font-weight:700;font-size:34px;color:var(--ink);line-height:1}
  .step h3{font-family:"Titillium Web",sans-serif;font-weight:700;font-size:20px;line-height:20px;color:#111;letter-spacing:.3px}
  .step p{font-size:12.6px;line-height:16.1px;color:var(--ink);margin-top:2px}
  .step.build{margin-top:20px}
  .step.breakthrough{margin-top:21px}
  .screen{position:absolute;left:317px;top:212px;width:561px;height:377px;border-radius:12px;background:#0d0d0d;border:2px solid #d9d9d9}
  .screen-inner{position:absolute;left:19px;top:21px;width:519px;height:327px;background:linear-gradient(120deg,#2a2a2a,#1b1b1b 55%,#242424)}
  .laptop-base{position:absolute;left:261px;top:589px;width:675px;height:38px;border-radius:0 0 22px 22px;background:linear-gradient(#f1f1f1,#bdbdbd)}
  .map{position:absolute;left:0;top:0}
  .node-label{font-family:"Titillium Web",sans-serif;font-weight:600;font-size:9px;fill:var(--gold);text-anchor:middle}
  .row-label{font-family:"Titillium Web",sans-serif;font-weight:700;font-size:12.5px;fill:var(--paper)}
  .row-num{font-family:"Lato",sans-serif;font-size:11px;fill:var(--paper);text-anchor:middle}
  .endpoint{font-family:"Lato",sans-serif;font-weight:700;font-size:18px;fill:var(--gold);text-anchor:middle}
</style>
</head>
<body>
<section class="flyer">
  <svg class="flyer-bg" width="1200" height="675" viewBox="0 0 1200 675" aria-hidden="true">
    <polygon points="0,0 46,0 600,350 102,675 0,675" fill="var(--gold-soft)"/>
    <polygon points="1145,0 1200,0 1200,675 1096,675 600,350" fill="var(--gold-soft)"/>
  </svg>

  <header class="brand">
    <div class="brand-mark"></div>
    <div class="brand-name"><span class="line-sm">KEYSTONE LADDER</span><span class="line-lg">METHOD</span></div>
  </header>

  <p class="tagline">A Clear Three Step Roadmap that will finally allow you<br>to attract quality customers and win more jobs.</p>

  <div class="intro">
    <p>The Keystone Ladder Method is a simple to follow system that was created specifically for Contractors and Blue Collar Business Owners.</p>
    <p>When it comes to marketing and growing their business, the majority of Contractors are left confused, frustrated and extremely overwhelmed. Unlike most sales, marketing &amp; training programs that offer a single "piece of the puzzle", we've mapped out each essential step of the puzzle and cut out all of the fluff.</p>
    <p class="cta">All you have to do is complete each step in the right order and we'll be guiding you along the entire journey!</p>
  </div>

  <div class="steps">
    <div class="step blueprint">
      <span class="step-num">1</span>
      <h3>BLUEPRINT:</h3>
      <p>Get clear on where you're going, define your ideal audience, and finally, master your message.</p>
    </div>
    <div class="step build">
      <span class="step-num">2</span>
      <h3>BUILD:</h3>
      <p>Attract quality leads, Build your funnel and Formulate a high-converting follow-up system</p>
    </div>
    <div class="step breakthrough">
      <span class="step-num">3</span>
      <h3>BREAKTHROUGH:</h3>
      <p>Get in front of your ideal customers and rapidly scale your business by driving traffic and becoming the authority in your market</p>
    </div>
  </div>

  <div class="screen"><div class="screen-inner"></div></div>
  <div class="laptop-base" role="img" aria-label="Silver laptop base"></div>

  <svg class="map" width="1200" height="675" viewBox="0 0 1200 675">
    <defs>
      <radialGradient id="iconTone" cx="50%" cy="45%" r="60%">
        <stop offset="0" stop-color="#f2d582"/>
        <stop offset="1" stop-color="#8b8c90"/>
      </radialGradient>
    </defs>
    <g stroke="#bdbdbd" stroke-width="1" stroke-dasharray="4 3" fill="none">
      <line x1="514" y1="296" x2="757" y2="296"/>
      <line x1="514" y1="397" x2="757" y2="397"/>
      <line x1="514" y1="505" x2="757" y2="505"/>
      <line x1="757" y1="397" x2="757" y2="505"/>
      <line x1="514" y1="296" x2="514" y2="397"/>
    </g>
    <g stroke="#d9d9d9" stroke-width="1" fill="none">
      <line x1="400" y1="528" x2="496" y2="523" transform="rotate(0)" opacity="0"/>
      <line x1="400" y1="532" x2="500" y2="522" opacity="0"/>
      <line x1="398" y1="532" x2="506" y2="522" opacity="0"/>
      <line x1="397" y1="535" x2="505" y2="524" opacity="0"/>
    </g>
    <line x1="397" y1="535" x2="496" y2="523" stroke="none"/>
    <line x1="396" y1="534" x2="505" y2="524" stroke="none"/>
    <line x1="398" y1="533" x2="499" y2="521" stroke="none"/>
    <line x1="399" y1="530" x2="497" y2="520" stroke="none"/>
    <path d="M398 532 L409 519" stroke="#d9d9d9" stroke-width="1" fill="none"/>
    <path d="M779 284 Q800 272 816 266 M810 262 L817 266 L811 271" stroke="#d9d9d9" stroke-width="1.2" fill="none"/>
    <text class="endpoint" x="393" y="548">A</text>
    <text class="endpoint" x="838" y="274">B</text>

    <g>
      <rect x="355" y="282" width="16" height="18" rx="2" fill="none" stroke="var(--gold)" stroke-width="1.5"/>
      <text class="row-num" x="363" y="295">3</text>
      <text class="row-label" x="376" y="295">BREAKTHROUGH</text>
      <line x1="376" y1="299" x2="465" y2="299" stroke="var(--gold)" stroke-width="2"/>

      <rect x="355" y="387" width="16" height="18" rx="2" fill="none" stroke="var(--gold)" stroke-width="1.5"/>
      <text class="row-num" x="363" y="400">2</text>
      <text class="row-label" x="376" y="400">BUILD</text>
      <line x1="376" y1="404" x2="415" y2="404" stroke="var(--gold)" stroke-width="2"/>

      <rect x="355" y="494" width="16" height="18" rx="2" fill="none" stroke="var(--gold)" stroke-width="1.5"/>
      <text class="row-num" x="363" y="507">1</text>
      <text class="row-label" x="376" y="507">BLUEPRINT</text>
      <line x1="376" y1="511" x2="436" y2="511" stroke="var(--gold)" stroke-width="2"/>
    </g>

    <text class="node-label" x="514" y="262">Turn-On the Traffic</text>
    <text class="node-label" x="650" y="262">Become the Authority</text>
    <text class="node-label" x="757" y="262">Unlock Your Growth</text>
    <text class="node-label" x="514" y="362">Formulate the Follow-Up</text>
    <text class="node-label" x="650" y="362">Construct Your Funnel</text>
    <text class="node-label" x="757" y="362">Develop Lead Generator</text>
    <text class="node-label" x="514" y="469">Clarify the Chaos</text>
    <text class="node-label" x="650" y="469">Define Your Customer</text>
    <text class="node-label" x="757" y="469">Master Your Message</text>

    <g fill="var(--paper)">
      <circle cx="514" cy="296" r="28"/><circle cx="650" cy="296" r="28"/><circle cx="757" cy="296" r="28"/>
      <circle cx="514" cy="397" r="28"/><circle cx="650" cy="397" r="28"/><circle cx="757" cy="397" r="28"/>
      <circle cx="514" cy="505" r="28" stroke="var(--gold)" stroke-width="4"/><circle cx="650" cy="505" r="28"/><circle cx="757" cy="505" r="28"/>
    </g>
    <g fill="url(#iconTone)">
      <circle role="img" aria-label="Web page icon" cx="514" cy="296" r="17"/>
      <circle role="img" aria-label="Mountain summit icon" cx="650" cy="296" r="17"/>
      <circle role="img" aria-label="Rocket launch icon" cx="757" cy="296" r="17"/>
      <circle role="img" aria-label="Follow-up list icon" cx="514" cy="397" r="17"/>
      <circle role="img" aria-label="Funnel icon" cx="650" cy="397" r="17"/>
      <circle role="img" aria-label="Magnet icon" cx="757" cy="397" r="17"/>
      <circle role="img" aria-label="Target icon" cx="514" cy="505" r="17"/>
      <circle role="img" aria-label="Customer icon" cx="650" cy="505" r="17"/>
      <circle role="img" aria-label="Megaphone icon" cx="757" cy="505" r="17"/>
    </g>
  </svg>
</section>
</body>
</html>
```